Brightfold Sky Advisors needs a wordpress design

New consulting company based in San Francisco focusing on leading businesses (primarily startups) into the cloud. Services include: cloud architecture, security, automation, back-end design, Infrastructure Optimization, Capacity Planning. Even though we are a new company, I'd like to convey a sense of confidence to the prospective client. Logos are attached

Target Market(s)

Start-ups looking to move their application into the cloud

Industry/Entity Type

Information Technology

```html
<!DOCTYPE html>
<html lang="en">
<head>
<meta charset="utf-8">
<title>Brightfold Sky Advisors</title>
<link href="https://fonts.googleapis.com/css2?family=Open+Sans:wght@400;600;700&display=swap" rel="stylesheet">
<style>
:root{
  --blue:#1a87c9;
  --blue-dark:#136fa8;
  --red:#e3342a;
  --ink:#333a40;
  --muted:#8a9096;
  --line:#dfe3e6;
  --band:#eef1f4;
  --white:#ffffff;
  --footer:#ffffff;
}
*{box-sizing:border-box;margin:0;padding:0}
html,body{width:1200px;height:3380px;overflow:hidden}
body{font-family:"Open Sans",Arial,sans-serif;color:var(--ink);background:var(--white);position:relative}

/* hero */
.hero{position:absolute;left:0;top:0;width:1200px;height:760px;overflow:hidden}
.hero-photo{position:absolute;inset:0;background:linear-gradient(180deg,#dfe6ee 0%,#c9cdd4 30%,#b89c8c 60%,#a88274 80%,#c6b0a4 100%)}
.hero-photo::after{content:"";position:absolute;inset:0;background:linear-gradient(90deg,rgba(255,255,255,0) 40%,rgba(255,255,255,.45) 100%)}
.brand{display:flex;align-items:center;gap:12px}
.hero .brand{position:absolute;left:40px;top:40px}
.brand-dot{flex:0 0 30px;width:30px;height:30px;border-radius:50%;background:var(--blue)}
.brand-name{font-size:22px;font-weight:700;color:var(--blue-dark);line-height:1.1;white-space:nowrap}
.nav{position:absolute;right:60px;top:48px;display:flex;gap:10px}
.nav a{font-size:15px;color:var(--ink);text-decoration:none;padding:6px 16px;border-radius:16px}
.nav a.active{background:var(--blue);color:var(--white)}
.hero-copy{position:absolute;left:600px;top:276px;width:500px}
.hero-copy h1{font-size:34px;font-weight:600;color:var(--blue);line-height:1.3;text-align:right}
.hero-copy h1 span{display:block;white-space:nowrap}
.hero-copy p{margin:20px 0 0 70px;font-size:14px;line-height:1.6;color:var(--white);text-align:right;text-shadow:0 1px 2px rgba(0,0,0,.3)}
.btn{display:inline-block;background:var(--red);color:var(--white);font-size:14px;font-weight:600;text-transform:uppercase;padding:10px 26px;border-radius:20px;text-decoration:none}
.hero-copy .btn{position:absolute;right:0;top:240px}
.slider-arrow{position:absolute;top:390px;width:36px;height:36px;border-radius:50%;background:rgba(255,255,255,.5)}

/* section titles */
.kicker{font-size:13px;text-transform:uppercase;color:var(--muted);text-align:center;letter-spacing:1px}
.section-title{font-size:30px;font-weight:700;text-transform:uppercase;color:var(--blue);text-align:center;letter-spacing:1px}
.title-rule{width:8px;height:8px;border-radius:50%;background:var(--blue);margin:10px auto 0}

/* services */
.services{position:absolute;left:0;top:760px;width:1200px;height:560px}
.services .kicker{margin-top:60px}
.service-grid{position:absolute;left:112px;top:152px;width:976px;display:grid;grid-template-columns:repeat(3,1fr);gap:64px 40px}
.service{display:flex;gap:16px;border:1px solid var(--line);height:136px;padding:22px 18px;background:var(--white)}
.service.featured{background:var(--blue);color:var(--white);border-color:var(--blue);box-shadow:-24px 0 0 0 var(--blue)}
.service-icon{flex:0 0 40px;height:40px;display:flex;align-items:center;justify-content:center}
.service h3{font-size:13px;font-weight:700;text-transform:uppercase;line-height:1.35;margin-bottom:6px}
.service p{font-size:12px;line-height:1.55;color:var(--muted)}
.service.featured p{color:#d8ebf7}

/* band */
.band{position:absolute;left:0;top:1336px;width:1200px;height:100px;background:var(--band);display:flex;align-items:center;padding:0 100px;gap:60px}
.band p{font-size:14px;line-height:1.6;color:var(--ink);flex:1}
.band .btn{font-size:13px;padding:10px 34px}

/* portfolio */
.portfolio{position:absolute;left:0;top:1500px;width:1200px}
.tabs{display:flex;justify-content:center;gap:44px;margin-top:40px;font-size:12px;text-transform:uppercase;color:var(--ink)}
.tabs span{padding-bottom:10px}
.tabs span.active{border-bottom:2px solid var(--blue)}
.tabs-line{width:776px;height:1px;background:var(--line);margin:0 auto}
.works{position:absolute;left:212px;top:200px;width:888px}
.works-row{display:grid;gap:16px}
.works-row.two{grid-template-columns:1fr 1fr}
.works-row.three{grid-template-columns:1fr 1fr 1fr;margin-top:26px}
.work-img{width:100%}
.two .work-img{height:332px}
.three .work-img{height:268px}
.work figcaption{text-align:center;padding-top:12px}
.work strong{display:block;font-size:12px;font-weight:700;text-transform:uppercase}
.work em{font-style:normal;font-size:11px;color:var(--muted)}
.work figcaption::after{content:"";display:block;width:140px;height:1px;background:var(--line);margin:10px auto 0}
.view-all{position:absolute;left:518px;top:1000px;font-size:13px;padding:10px 40px;border-radius:4px}

/* partners */
.partners{position:absolute;left:0;top:2628px;width:1200px;height:184px;background:var(--band);display:flex;justify-content:center;align-items:center;gap:68px}
.partner{width:64px;height:40px;background:#c5ccd2;border-radius:4px}
.partner.round{width:48px;height:48px;border-radius:50%}

/* cta */
.cta{position:absolute;left:0;top:2812px;width:1200px;height:200px;background:var(--blue);text-align:center;color:var(--white);padding-top:48px}
.cta h2{font-size:34px;font-weight:400}
.cta p{font-size:13px;color:#cfe6f5;margin-top:2px}
.cta .btn-outline{display:inline-block;margin-top:14px;background:var(--white);color:var(--blue);font-size:14px;font-weight:600;text-transform:uppercase;padding:8px 30px;letter-spacing:1px;text-decoration:none}

/* footer */
.footer{position:absolute;left:0;top:3012px;width:1200px;height:368px;background:var(--footer)}
.foot-brand{position:absolute;left:100px;top:44px;width:220px}
.foot-brand .brand-name{font-size:18px}
.foot-brand p{font-size:12px;line-height:1.6;color:var(--muted);margin-top:22px}
.foot-col{position:absolute;top:44px;width:220px}
.foot-col h4{font-size:20px;font-weight:600;text-transform:uppercase;letter-spacing:1px;padding-bottom:8px;border-bottom:3px solid var(--ink)}
.foot-col ul{list-style:none;margin-top:14px}
.foot-col li{font-size:12px;color:var(--muted);line-height:2.1}
.subscribe{display:flex;margin-top:28px}
.subscribe span{flex:1;border:1px solid var(--line);font-size:12px;color:var(--muted);padding:10px}
.subscribe b{background:var(--red);color:var(--white);font-size:12px;font-weight:600;padding:10px 14px}
.foot-bar{position:absolute;left:100px;right:100px;top:316px;border-top:1px solid var(--line);padding-top:10px;display:flex;justify-content:space-between;font-size:11px;color:var(--muted)}
.foot-bar span+span{margin-left:20px}
</style>
</head>
<body>

<header class="hero">
  <div class="hero-photo" role="img" aria-label="Aerial photograph of a city skyline at sunrise"></div>
  <div class="brand"><span class="brand-dot"></span><span class="brand-name">Brightfold Sky<br>Advisors</span></div>
  <nav class="nav">
    <a class="active" href="#">Home</a><a href="#">About Us</a><a href="#">Services</a><a href="#">Portfolio</a><a href="#">Gallery</a><a href="#">Testimonial</a><a href="#">Contact Us</a>
  </nav>
  <span class="slider-arrow" style="left:20px"></span>
  <span class="slider-arrow" style="right:20px"></span>
  <div class="hero-copy">
    <h1><span>We provide cloud consulting</span><span>services</span></h1>
    <p>Lorem ipsum dolor sit amet, consectetur adipiscing elit. Ut fermentum eget sem sed porttitor. Phasellus mauris molestie ligula, sed commodo turpis accumsan pulvinar. Aliquam erat volutpat.</p>
    <a class="btn" href="#">Read More</a>
  </div>
</header>

<section class="services">
  <p class="kicker">Our what we offer</p>
  <h2 class="section-title">Our Services</h2>
  <div class="title-rule"></div>
  <div class="service-grid">
    <article class="service featured">
      <div class="service-icon"><svg width="36" height="26" viewBox="0 0 36 26"><path d="M9 24h19a7 7 0 0 0 0-14 10 10 0 0 0-19 2 6 6 0 0 0 0 12z" fill="none" stroke="#fff" stroke-width="2.5"/></svg></div>
      <div><h3>Cloud Architecture</h3><p>Lorem ipsum dolor sit amet, consectetur adipiscing elit sed do eiusmod.</p></div>
    </article>
    <article class="service">
      <div class="service-icon"><svg width="20" height="24" viewBox="0 0 20 24"><rect x="2" y="10" width="16" height="13" rx="2" fill="#555"/><path d="M5 10V7a5 5 0 0 1 10 0v3" fill="none" stroke="#555" stroke-width="2.5"/></svg></div>
      <div><h3>Security</h3><p>Lorem ipsum dolor sit amet, consectetur adipiscing elit sed do eiusmod.</p></div>
    </article>
    <article class="service">
      <div class="service-icon"><svg width="28" height="20" viewBox="0 0 28 20"><path d="M3 12l3-8h16l3 8v6H3z" fill="#555"/><circle cx="8" cy="14" r="2" fill="#fff"/><circle cx="20" cy="14" r="2" fill="#fff"/></svg></div>
      <div><h3>Automation</h3><p>Lorem ipsum dolor sit amet, consectetur adipiscing elit sed do eiusmod.</p></div>
    </article>
    <article class="service">
      <div class="service-icon"><svg width="28" height="28" viewBox="0 0 28 28"><circle cx="10" cy="12" r="6" fill="none" stroke="#555" stroke-width="3"/><circle cx="20" cy="20" r="4" fill="none" stroke="#555" stroke-width="2.5"/></svg></div>
      <div><h3>Back-End Design</h3><p>Lorem ipsum dolor sit amet, consectetur adipiscing elit sed do eiusmod.</p></div>
    </article>
    <article class="service">
      <div class="service-icon"><svg width="26" height="26" viewBox="0 0 26 26"><rect x="3" y="3" width="20" height="20" fill="none" stroke="#555" stroke-width="2.5"/><path d="M8 13h10M13 8v10" stroke="#555" stroke-width="2.5"/></svg></div>
      <div><h3>Infrastructure Optimization</h3><p>Lorem ipsum dolor sit amet, consectetur adipiscing elit.</p></div>
    </article>
    <article class="service">
      <div class="service-icon"><svg width="26" height="24" viewBox="0 0 26 24"><rect x="2" y="14" width="5" height="9" fill="#555"/><rect x="10" y="8" width="5" height="15" fill="#555"/><rect x="18" y="2" width="5" height="21" fill="#555"/></svg></div>
      <div><h3>Capacity Planning</h3><p>Lorem ipsum dolor sit amet, consectetur adipiscing elit sed do eiusmod.</p></div>
    </article>
  </div>
</section>

<section class="band">
  <p>Suspendisse aliquet elit nec ipsum commodo, ac ornare ligula fermentum. Cras id libero vitae erat elementum tincidunt sit amet ut nisi. Nam erat leo, semper et tortor id, commodo porttitor nisi.</p>
  <a class="btn" href="#">Join with us</a>
</section>

<section class="portfolio">
  <p class="kicker">Awesome works by us</p>
  <h2 class="section-title">Portfolio</h2>
  <div class="title-rule"></div>
  <div class="tabs"><span class="active">All</span><span>Cloud</span><span>Capacity Planning</span><span>Back-end Design</span><span>Security</span></div>
  <div class="tabs-line"></div>
  <div class="works">
    <div class="works-row two">
      <figure class="work"><div class="work-img" role="img" aria-label="Photo of a hand touching a cloud network diagram" style="background:linear-gradient(135deg,#9aa4ad,#4b545c)"></div><figcaption><strong>Cmmi blandit neque molestie</strong><em>Cras tincidunt</em></figcaption></figure>
      <figure class="work"><div class="work-img" role="img" aria-label="Photo of a businessman pointing at a screen" style="background:linear-gradient(135deg,#6b5a4c,#2e2824)"></div><figcaption><strong>Cmmi blandit neque molestie</strong><em>Cras tincidunt</em></figcaption></figure>
    </div>
    <div class="works-row three">
      <figure class="work"><div class="work-img" role="img" aria-label="Photo of a digital security lock graphic" style="background:linear-gradient(135deg,#8fc3dd,#2f7fa8)"></div><figcaption><strong>Cmmi blandit neque molestie</strong><em>Cras tincidunt</em></figcaption></figure>
      <figure class="work"><div class="work-img" role="img" aria-label="Photo of hands typing on a laptop" style="background:linear-gradient(135deg,#5d7da0,#2a3540)"></div><figcaption><strong>Cmmi blandit neque molestie</strong><em>Cras tincidunt</em></figcaption></figure>
      <figure class="work"><div class="work-img" role="img" aria-label="Photo of a padlock on a keyboard" style="background:linear-gradient(135deg,#5f96b8,#1e3e55)"></div><figcaption><strong>Cmmi blandit neque molestie</strong><em>Cras tincidunt</em></figcaption></figure>
    </div>
  </div>
  <a class="btn view-all" href="#">View All</a>
</section>

<section class="partners" aria-label="Partners">
  <span class="partner round"></span><span class="partner"></span><span class="partner round"></span><span class="partner"></span><span class="partner"></span><span class="partner round"></span><span class="partner"></span>
</section>

<section class="cta">
  <h2>Lorem ipsum dolor sit amet, consectetur</h2>
  <p>Suspendisse aliquet elit nec ipsum commodo</p>
  <a class="btn-outline" href="#">Contact Now</a>
</section>

<footer class="footer">
  <div class="foot-brand">
    <div class="brand"><span class="brand-dot"></span><span class="brand-name">Brightfold Sky<br>Advisors</span></div>
    <p>Morbi scelerisque volutpat ex quis ultricies. Sed commodo augue nec diam facilisis pellentesque. Ut tincidunt scelerisque ex eu posuere. Phasellus iaculis eu odio ligula, non commodo lorem.</p>
  </div>
  <div class="foot-col" style="left:352px"><h4>About</h4><ul><li>Home</li><li>About Us</li><li>Services</li><li>Portfolio</li><li>Gallery</li><li>Testimonial</li><li>Contact Us</li></ul></div>
  <div class="foot-col" style="left:608px"><h4>Our Works</h4><ul><li>Computers</li><li>Mobile Applications</li><li>Website</li><li>Digital Production</li><li>Installations</li><li>Fields</li></ul></div>
  <div class="foot-col" style="left:868px"><h4>Our Works</h4><div class="subscribe"><span>Your Email Address</span><b>Sign Up</b></div></div>
  <div class="foot-bar"><span>© 2015 Brightfold. All Rights Reserved</span><div><span>Terms of Use</span><span>Privacy Policy</span></div></div>
</footer>

</body>
</html>
```